Global Developmental Delay Awareness Day Poster

I need a poster to raise awareness for a condition called Global Developmental Delay (GDD) . The day of awareness for this condition is May 1. The condition is something found in children who are significantly delayed in their milestones. We are hopeful that through education and support more children with this condition can gain access to therapies and support to minimize the long term effects and maxamise their potential. Theme for GDD awareness is yellow so lots of yellow needed. Can be any yellow. Like it to be colourful, but not bright if that makes sense. I'd like it to be classy but fun and childish - this is a childhood diagnosis. Just not 'tacky'. Like the design to reflect the wonders of childhood so feel free to use your imagination!

Target Market(s)

Mums (and dads) of young children under 5

Colors
fee18a
fbf289

Requirements
Must have
• cheery, childish, happy feel - see uploaded poster examples for ideas. They are just ideas for theme. Different fun, childish fonts and 'sections' - perhaps with different colour backgrounds etc.
• Heading should be "Global Developmental Delay" or something similar
• Must have text as in the attachment
• Must have yellow 'theme'
• more colours than just yellow.
Nice to have
• colors - not bright but colorful.

```html
<!DOCTYPE html>
<html lang="en">
<head>
<meta charset="utf-8">
<title>Global Developmental Delay</title>
<link href="https://fonts.googleapis.com/css2?family=Sniglet:wght@400;800&family=Raleway:wght@300;400;700&display=swap" rel="stylesheet">
<style>
  :root {
    --orange-top: #f07c2c;
    --orange-mid: #f6a531;
    --sun-yellow: #fee18a;
    --pale-yellow: #fbf289;
    --grass-light: #9cc23c;
    --grass-mid: #7aa83a;
    --grass-dark: #4f7a2e;
    --ink: #ffffff;
    --card: #ffffff;
  }
  * { margin: 0; padding: 0; box-sizing: border-box; }
  html, body { width: 849px; height: 1200px; overflow: hidden; }
  body { font-family: "Raleway", sans-serif; color: var(--ink); }
  .poster {
    position: relative; width: 849px; height: 1200px; overflow: hidden;
    background: linear-gradient(180deg, var(--orange-top) 0%, var(--orange-mid) 18%, var(--sun-yellow) 42%, var(--pale-yellow) 50%);
  }
  .hill { position: absolute; left: 0; top: 0; width: 849px; height: 1200px; }
  .scene {
    position: absolute; left: 20px; top: 270px; width: 809px; height: 340px;
    background: radial-gradient(ellipse at 50% 60%, rgba(255,250,215,0.9) 0%, rgba(254,225,138,0.6) 45%, rgba(246,165,49,0) 75%);
    border-radius: 40px;
  }
  .title {
    position: absolute; left: 0; top: 22px; width: 849px; text-align: center;
    font-family: "Sniglet", cursive; font-weight: 800; line-height: 0.82;
    text-shadow: 0 2px 6px rgba(180,80,0,0.25);
  }
  .title span { display: block; }
  .title .t1 { font-size: 66px; margin-left: 4px; }
  .title .t2 { font-size: 74px; transform: rotate(2deg); margin-top: 4px; }
  .title .t3 { font-size: 70px; margin-top: 4px; }
  .col { position: absolute; font-size: 16.5px; line-height: 17.6px; font-weight: 400; }
  .col-left { left: 42px; top: 655px; width: 366px; }
  .col-right { left: 439px; top: 655px; width: 377px; }
  .col h2 { font-weight: 700; font-size: 18px; margin-bottom: 16px; }
  .col p { text-align: justify; }
  .col-left p { padding-left: 0; }
  .bullets { list-style: none; margin-left: -14px; margin-top: 10px; }
  .bullets li { position: relative; padding-left: 28px; height: 26.5px; line-height: 26.5px; font-size: 17px; }
  .bullets li::before {
    content: ""; position: absolute; left: 10px; top: 9px; width: 10px; height: 10px;
    border-radius: 50%; background: var(--ink);
  }
  .causes li { height: 28.5px; line-height: 28.5px; }
  .gap { margin-top: 16px; }
  .contact-label { margin-top: 19px; font-size: 17px; }
  .contact-box {
    position: absolute; left: 439px; top: 1120px; width: 386px; height: 58px;
    background: var(--card); border-radius: 10px;
  }
</style>
</head>
<body>
<main class="poster">
  <svg class="hill" viewBox="0 0 849 1200" aria-hidden="true">
    <defs>
      <linearGradient id="grass" x1="0" y1="0" x2="0" y2="1">
        <stop offset="0" stop-color="#b9cf45"/>
        <stop offset="0.35" stop-color="#8fb63c"/>
        <stop offset="1" stop-color="#4f7a2e"/>
      </linearGradient>
    </defs>
    <path d="M0 640 C 200 585, 650 570, 849 625 L 849 1200 L 0 1200 Z" fill="url(#grass)"/>
  </svg>

  <h1 class="title">
    <span class="t1">Global</span>
    <span class="t2">Developmental</span>
    <span class="t3">Delay</span>
  </h1>

  <div class="scene" role="img" aria-label="Illustration of six happy cartoon children holding hands and jumping over a grassy hill in front of a glowing sun"></div>

  <section class="col col-left">
    <h2>What is GDD?</h2>
    <p>A developmental delay is more than being “a little behind.” Global developmental delay (GDD) is diagnosed when a child is significantly delayed in two or more of the 5 developmental realms including,</p>
    <ul class="bullets">
      <li>Cognitive (or thinking)</li>
      <li>Social and emotional</li>
      <li>Communication</li>
      <li>Fine motor</li>
      <li>Gross motor</li>
    </ul>
    <h2 class="gap">What causes GDD?</h2>
    <p>There are many possible causes of GDD. Some are permanent, but others aren’t. They include:</p>
    <ul class="bullets causes">
      <li>Genetic conditions:</li>
      <li>Complications in pregnancy or birth:</li>
      <li>Environmental issues:</li>
      <li>Other medical conditions:</li>
    </ul>
  </section>

  <section class="col col-right">
    <p>More often than not a child received a secondary diagnosis as they grow such as intellectual disability or autism spectrum disorder, in which case the name for the disorder replaces the term developmental delay.</p>
    <h2 class="gap">If you are concerned</h2>
    <p>Early intervention programs and therapies can give many children with global development delays a head start and allow them to reach their full potential.If you are concerned that your child is not developing at the rate you would expect, please talk to your GP.</p>
    <h2 class="gap">What can you do?</h2>
    <p>Each child is different in their own wonderful way, if we choose to celebrate and understand the things that make us unique as well as the ones that bring us together, we can create a much happier and more inclusive environment for all our children.</p>
    <p class="contact-label">Looking for more info or support contact :</p>
  </section>

  <div class="contact-box"></div>
</main>
</body>
</html>
```